"Every Lantern Still Burning" Sermon Series Design

Needing a design for our church's next sermon series titled "Every Lantern Still Burning" where we will discuss the need for unity, diversity, love and clarity. Looking for a 1920 x 1080 (or higher res) editable and layered file (PSD or AI) so that we can reformat the design to work on social, screens, lower thirds and various print and online mediums. We will also need to have access to the font files so that we can make resize and tweak as needed. We like the idea of using a globe or map of the world as the backdrop with the words overtop. Or, the idea of creating a bunch of newspaper clippings (generic, so that they can't actually be read) and making the shape of a heart. See attached examples. This website will give you an idea of our previous sermon series designs so you can have an idea of our style (but, feel free to help us advance the ball on something more aligned with current design trends): https://www.brinmoorfellowship.church/series

Examples use red, but stay away from a ton of red. If you're gonna major in a color, use blue or something in that family.

Must haves:
Title: Every Lantern Still Burning
Tagline : (TBD - use some Lorem Ipsum as a placeholder and we will fill in later)
Our Logo (attached) (small towards bottom is standard - only use solid colors for logo - preferably just solid black or white)

Industry/Entity Type

Church

Font styles to use
Serif
Sans Serif

Requirements
Must have
• Title: Every Lantern Still Burning
Nice to have
• We like the idea of using a globe or map of the world as the backdrop with the words overtop. Or, the idea of creating a bunch of newspaper clippings (generic, so that they can't actually be read) and making the shape of a heart. See attached examples.

If you're gonna major on a color, stick with blue or something close.
Should not have
• Don't use red as the primary color (example we sent has red, but stay away from it)

```html
<!DOCTYPE html>
<html lang="en">
<head>
<meta charset="utf-8">
<title>Every Lantern Still Burning – Sermon Series</title>
<link href="https://fonts.googleapis.com/css2?family=Montserrat:wght@400;500;700&family=Lato:wght@400&display=swap" rel="stylesheet">
<style>
  :root {
    --page-bg: #ffffff;
    --card-top: #0c4cac;
    --card-mid: #0a3c8f;
    --card-bottom: #0a2556;
    --ink: #ffffff;
    --ink-soft: rgba(255, 255, 255, 0.85);
    --ghost: rgba(4, 28, 80, 0.35);
    --globe-light: #3f8fd8;
    --globe-dark: #0a2a66;
  }
  * { margin: 0; padding: 0; box-sizing: border-box; }
  html, body {
    width: 1200px;
    height: 1200px;
    overflow: hidden;
    background: var(--page-bg);
  }
  .series-card {
    position: absolute;
    left: 104px;
    top: 322px;
    width: 1001px;
    height: 562px;
    overflow: hidden;
    background: linear-gradient(180deg, var(--card-top) 0%, var(--card-mid) 45%, var(--card-bottom) 100%);
    box-shadow: 2px 2px 3px rgba(0, 0, 0, 0.35);
    font-family: "Montserrat", sans-serif;
    color: var(--ink);
  }
  .ghost-ring {
    position: absolute;
    left: 18px;
    top: 56px;
    width: 318px;
    height: 318px;
  }
  .church-name {
    position: absolute;
    left: 386px;
    top: 50px;
    display: flex;
    align-items: center;
    gap: 12px;
  }
  .church-name__dot {
    width: 58px;
    height: 58px;
    border: 2px solid var(--ink);
    border-radius: 50%;
  }
  .church-name__text {
    font-weight: 500;
    font-size: 17px;
    letter-spacing: 4px;
    color: var(--ink);
  }
  .title-frame {
    position: absolute;
    left: 352px;
    top: 144px;
    width: 320px;
    height: 313px;
  }
  .globe-backdrop {
    position: absolute;
    left: 378px;
    top: 163px;
    width: 268px;
    height: 268px;
    border-radius: 50%;
    background: radial-gradient(circle at 50% 42%, var(--globe-light) 0%, #1f5fb0 40%, var(--globe-dark) 100%);
    box-shadow: 0 0 18px rgba(90, 170, 255, 0.35);
  }
  .series-title {
    position: absolute;
    left: 352px;
    top: 186px;
    width: 320px;
    text-align: center;
    font-weight: 700;
    font-size: 29px;
    line-height: 56px;
    color: var(--ink);
    text-shadow: 0 2px 6px rgba(0, 0, 0, 0.45);
  }
  .tagline {
    position: absolute;
    width: 330px;
    text-align: center;
    font-family: "Lato", sans-serif;
    font-size: 14.5px;
    color: var(--ink-soft);
    white-space: nowrap;
    transform: translate(-50%, -50%) rotate(-90deg);
  }
  .tagline--left { left: 290px; top: 305px; }
  .tagline--right { left: 738px; top: 304px; }
  .series-url {
    position: absolute;
    left: 0;
    top: 487px;
    width: 1024px;
    text-align: center;
    font-weight: 700;
    font-size: 19px;
    letter-spacing: 2.5px;
    color: var(--ink);
  }
</style>
</head>
<body>
  <main class="series-card">
    <svg class="ghost-ring" viewBox="0 0 318 318" aria-hidden="true">
      <circle cx="159" cy="159" r="150" fill="none" stroke="var(--ghost)" stroke-width="14"/>
    </svg>

    <div class="church-name">
      <span class="church-name__dot"></span>
      <span class="church-name__text">BRINMOOR FELLOWSHIP</span>
    </div>

    <div class="globe-backdrop" role="img" aria-label="Glowing blue globe of the world with network dots"></div>

    <svg class="title-frame" viewBox="0 0 320 313" aria-hidden="true">
      <polyline points="112,1.5 1.5,1.5 1.5,311.5 112,311.5" fill="none" stroke="var(--ink)" stroke-width="2"/>
      <polyline points="211,1.5 318.5,1.5 318.5,311.5 211,311.5" fill="none" stroke="var(--ink)" stroke-width="2"/>
    </svg>

    <h1 class="series-title">Every<br>Lantern<br>Still<br>Burning</h1>

    <p class="tagline tagline--left">of the printing and typesetting industry.</p>
    <p class="tagline tagline--right">Lorem Ipsum is simply dummy text</p>

    <p class="series-url">www.brinmoorfellowship.church</p>
  </main>
</body>
</html>
```